Illustrationen für ein Balance Boards
Zielgruppe
Meine Firma verkauft Balance Boards und Skateboards.
Ich habe meine Balance Board Designs von meinen anderen 2 Produkten verlinkt.
Ich verlinke hier einmal meine Produkte und dabei wird die Zielgruppe deutlich klarer anhand der Bewertungen usw.
1. https://www.kaufwelt-beispiel.de/dp/Q71TRM5XWA?ref=myi_title_dp
2. https://www.kaufwelt-beispiel.de/dp/Q71JNH4ZRE?ref=myi_title_dp
Es soll dabei ein neues Design erstellt werden für das Board, welches auf dem Karton liegt.
Es wäre dabei gut, wenn das Bild 3D gerendert wird oder einfach das Bild von der Konkurrenz verwendet wird.
Das ist nicht das gleiche Board, aber relativ ähnlich.
Aufgabenstellung
Wichtig beim Design ist das es leicht sein soll neue Varianten zu erstellen indem man einfach die Farbe verändert. Das sieht man anhand von meinen anderen Produkten.
Das Logo war zudem immer sehr dominant auf meinen Produkten, aber ich bin bereit neue Optionen zusehen.

```html
<!DOCTYPE html>
<html lang="de">
<head>
<meta charset="utf-8">
<title>FlowRise 360 – Banner</title>
<link rel="stylesheet" href="https://fonts.googleapis.com/css2?family=Russo+One&display=swap">
<style>
  :root {
    --ink: #000000;
    --coral: #fb5a5a;
    --smoke: #5c5c5c;
    --ash: #8a8a8a;
    --paper: #ffffff;
    --cream: #f4ede7;
  }
  html, body {
    margin: 0;
    padding: 0;
    overflow: hidden;
    background: var(--ink);
  }
  .banner {
    position: relative;
    width: 1200px;
    height: 284px;
    overflow: hidden;
    background: var(--ink);
  }
  .banner__shapes {
    position: absolute;
    inset: 0;
    width: 1200px;
    height: 284px;
  }
  .banner__brand {
    position: absolute;
    left: 212px;
    top: 92px;
    width: 760px;
    height: 100px;
    display: flex;
    align-items: center;
    justify-content: center;
    font-family: "Russo One", "Arial Black", sans-serif;
    font-size: 88px;
    line-height: 1;
    letter-spacing: 4px;
    color: var(--cream);
    white-space: nowrap;
  }
</style>
</head>
<body>
  <main class="banner">
    <svg class="banner__shapes" viewBox="0 0 1200 284" xmlns="http://www.w3.org/2000/svg" aria-hidden="false">
      <defs>
        <radialGradient id="mesh-glow" cx="50%" cy="50%" r="50%">
          <stop offset="0%" stop-color="#9a9a9a" stop-opacity="0.45"/>
          <stop offset="100%" stop-color="#9a9a9a" stop-opacity="0"/>
        </radialGradient>
      </defs>

      <!-- hatched band, top left -->
      <rect class="hatch-band" x="0" y="0" width="314" height="42" fill="var(--smoke)" opacity="0.55"
            role="img" aria-label="Diagonal hatch pattern band"/>

      <!-- dotted circle, left -->
      <circle class="dot-disc" cx="120" cy="171" r="88" fill="var(--smoke)" opacity="0.6"
              role="img" aria-label="Dot pattern circle"/>

      <!-- coral circle -->
      <circle class="accent-disc" cx="309" cy="143" r="162" fill="var(--coral)"/>

      <!-- wave mesh area -->
      <ellipse class="wave-mesh" cx="700" cy="142" rx="330" ry="150" fill="url(#mesh-glow)"
               role="img" aria-label="Flowing wireframe wave mesh"/>

      <!-- grey circle, bottom right -->
      <circle class="shade-disc" cx="738" cy="282" r="100" fill="var(--smoke)"/>

      <!-- dotted half circle, bottom -->
      <circle class="dot-disc" cx="600" cy="284" r="88" fill="var(--smoke)" opacity="0.6"
              role="img" aria-label="Dot pattern half circle"/>

      <!-- cross mark -->
      <g class="cross" fill="var(--paper)" transform="translate(1062 125) rotate(45)">
        <rect x="-74" y="-15" width="148" height="30"/>
        <rect x="-15" y="-74" width="30" height="148"/>
      </g>
    </svg>

    <div class="banner__brand">FlowRise 360</div>
  </main>
</body>
</html>
```